2018 Vision Board Workshop

I need to promote this workshop on both an 8.5x11 sheet and a 5x7 card. I do have a logo that needs to be present. I'd like to stay true to my branded colors. The flyer needs to project the excitement of a new year and the possibilities of what a person can create, produce, explore in their lives by putting it all on a vision board. Creating the vision of what you want will inspire you to achieve your goals and dreams. Looking at your vision board each day will propel you into taking action as you chart your course to achieve what you truly want.
The flyer needs to have the following information:
The workshop date and time - Sat., Jan. 13, 2018, 10:30-1:30
The location is - Atrium 47B, 2864 Birchwood Vale Rd, Colorado Springs, Co 80417
in the FORGE Room
My name and contact information - Mara Vollbeck
Text and voice 303-417-6652
Email - mara@brightwell-daily-craft.com
Website - brightwell-daily-craft.com
The fee is $45. All materials are provided.

My company is called Brightwell Daily Craft. I am a Life Coach, author, speaker and workshop leader.\ I wrote this program, Brightwell Daily Craft to teach concepts and supporting skills for living with more happiness, satisfaction and fulfillment. Thanks for reading this!! Mara

Target Market(s)

Primarily women, educated, motivated, proactive in their own lives and well being

Font styles to use
Other font styles liked:
• I have been using Century Gothic. I'm open to new ideas.

Requirements
Must have
• The Brightwell Daily Craft logo
• The flyer needs to have the following information:
• The workshop date and time - Sat., Jan. 13, 2018, 10:30-1:30
• The location is - Atrium 47B, 2864 Birchwood Vale Rd, Colorado Springs, Co 80417
• in the FORGE Room
• My name and contact information - Mara Vollbeck
• Text and voice 303-417-6652
• Email - mara@brightwell-daily-craft.com
• Website - brightwell-daily-craft.com
• The fee is $45. All materials are provided.
Nice to have
• The Brightwell Daily Craft branded colors in the design
• Images of vision boards

```html
<!DOCTYPE html>
<html lang="en">
<head>
<meta charset="utf-8">
<title>Get Happier in 2018 – Workshop Flyer</title>
<link rel="stylesheet" href="https://fonts.googleapis.com/css2?family=Poppins:wght@400;600;800&family=Questrial&display=swap">
<style>
  :root {
    --page-bg: #e9e4dc;
    --paper: #ffffff;
    --brand-blue: #1e88f0;
    --sky-blue: #20aaf5;
    --brand-green: #7fd11b;
    --deep-green: #5fb30f;
    --ink: #2b2b2b;
    --muted-grey: #8c8c8c;
    --photo-top: #3f5a36;
    --photo-mid: #8a6a55;
    --photo-low: #cfd9e6;
  }
  * { margin: 0; padding: 0; box-sizing: border-box; }
  html, body { width: 1090px; height: 1200px; overflow: hidden; background: var(--page-bg); }
  .flyer {
    position: absolute; left: 96px; top: 20px;
    width: 1058px; height: 1368px;
    background: var(--paper);
    transform: scale(0.848); transform-origin: top left;
    box-shadow: 0 6px 24px rgba(0,0,0,.25);
    overflow: hidden;
    font-family: "Questrial", sans-serif; color: var(--ink);
  }
  .hero, .footer-wave { position: absolute; left: 0; top: 0; }
  .headline {
    position: absolute; top: 700px; width: 100%; text-align: center;
    font-family: "Poppins", sans-serif; font-weight: 800; font-size: 68px;
    color: var(--brand-green); text-shadow: 3px 3px 0 #2f3a20;
  }
  .date-box {
    position: absolute; left: 280px; top: 802px; width: 536px; height: 110px;
    border-radius: 10px; border: 2px solid #0f6fd0;
    background: linear-gradient(#5fb6ff 0%, #2a93f5 48%, #1a7fe8 52%, #2b8ff0 100%);
    color: #fff; text-align: center;
    box-shadow: 0 18px 14px -12px rgba(0,0,0,.45);
  }
  .date-box .date { font-size: 37px; margin-top: 8px; }
  .date-box .time { font-size: 28px; margin-top: 2px; }
  .date-box b { font-family: "Poppins", sans-serif; font-weight: 600; }
  .date-box sup { font-size: 18px; }
  .where-icon { position: absolute; left: 53px; top: 969px; }
  .where-title {
    position: absolute; left: 182px; top: 958px;
    font-family: "Poppins", sans-serif; font-weight: 600; font-size: 34px; color: var(--brand-blue);
  }
  .where-address { position: absolute; left: 182px; top: 1008px; width: 305px; font-size: 17px; line-height: 23px; }
  .divider { position: absolute; left: 495px; top: 946px; width: 1px; height: 158px; background: #555; }
  .portrait {
    position: absolute; left: 513px; top: 957px; width: 150px; height: 150px; border-radius: 50%;
    border: 4px solid var(--brand-green);
    background: radial-gradient(circle at 50% 45%, #e8c9a8 0 28%, #d49a3c 45%, #b86a24 100%);
  }
  .contact-name {
    position: absolute; right: 62px; top: 970px;
    font-family: "Poppins", sans-serif; font-weight: 600; font-size: 35px; color: var(--brand-blue);
  }
  .contact-phone {
    position: absolute; left: 718px; top: 1020px;
    font-family: "Poppins", sans-serif; font-weight: 600; font-size: 39px; color: var(--ink);
  }
  .contact-email { position: absolute; left: 718px; top: 1072px; font-size: 19px; }
  .contact-icon { position: absolute; left: 676px; }
  .price-badge {
    position: absolute; left: 43px; top: 1097px; width: 222px; height: 222px; border-radius: 50%;
    background: radial-gradient(circle at 45% 35%, #a6e34a, var(--deep-green) 75%);
    border: 4px dotted #9bd64a; box-shadow: 0 0 0 5px #d6efb4;
    color: #fff; text-align: center; z-index: 2;
  }
  .price-badge::after {
    content: ""; position: absolute; inset: 14px; border-radius: 50%; border: 2px solid rgba(255,255,255,.7);
  }
  .price-badge .price {
    font-family: "Poppins", sans-serif; font-weight: 800; font-size: 62px; line-height: 1;
    margin-top: 50px; text-shadow: 2px 2px 0 rgba(0,0,0,.35);
  }
  .price-badge .note { font-size: 19px; line-height: 24px; margin-top: 8px; }
  .brand-name {
    position: absolute; top: 1192px; width: 100%; padding-left: 60px; text-align: center;
    font-size: 40px; color: var(--brand-green);
  }
  .brand-name .mark {
    display: inline-block; width: 22px; height: 22px; border-radius: 50%;
    background: var(--sky-blue); margin-right: 14px; vertical-align: 4px;
  }
  .website {
    position: absolute; top: 1302px; width: 100%; text-align: center;
    font-size: 41px; color: #fff; z-index: 1;
  }
  .website svg { vertical-align: -4px; margin-right: 14px; }
</style>
</head>
<body>
<div class="flyer">
  <svg class="hero" width="1058" height="720" viewBox="0 0 1058 720">
    <defs>
      <linearGradient id="photoTones" x1="0" y1="0" x2="0" y2="1">
        <stop offset="0" stop-color="var(--photo-top)"/>
        <stop offset="0.45" stop-color="var(--photo-mid)"/>
        <stop offset="1" stop-color="var(--photo-low)"/>
      </linearGradient>
    </defs>
    <path role="img" aria-label="Photo of a smiling family of four, two children riding piggyback on their parents outdoors"
          d="M0,0 H1058 V440 C970,560 790,672 540,680 C300,686 120,560 76,356 C55,368 25,372 0,372 Z" fill="url(#photoTones)"/>
    <path class="arc-curl-left" d="M0,362 C60,364 110,330 126,262" fill="none" stroke="var(--sky-blue)" stroke-width="22" stroke-linecap="round"/>
    <path class="arc-main" d="M80,352 C125,560 300,686 540,680 C790,672 970,560 1058,440" fill="none" stroke="var(--sky-blue)" stroke-width="24"/>
    <path class="arc-curl-right" d="M1058,438 C1000,430 952,390 948,322" fill="none" stroke="var(--sky-blue)" stroke-width="22" stroke-linecap="round"/>
    <path d="M104,346 C150,540 315,664 540,660 C780,654 955,548 1040,430" fill="none" stroke="#fff" stroke-width="4"/>
  </svg>

  <h1 class="headline">GET HAPPIER IN 2018</h1>

  <div class="date-box">
    <p class="date">Saturday, <b>13<sup>th</sup></b> January, <b>2018</b></p>
    <p class="time">Time- <b>10:30 - 1:30</b></p>
  </div>

  <svg class="where-icon" width="104" height="86" viewBox="0 0 104 86" aria-hidden="true">
    <path d="M52,4 L2,46 L12,50 L52,17 L92,50 L102,46 L82,29 V6 H72 V21 Z" fill="var(--muted-grey)"/>
    <path d="M18,50 L52,22 L86,50 V84 H62 V60 H42 V84 H18 Z" fill="var(--muted-grey)"/>
  </svg>
  <h2 class="where-title">Where</h2>
  <p class="where-address">Atrium 47B, 2864 Birchwood Vale Rd,<br>Colorado Springs, Co 80417<br>in the FORGE Room</p>

  <div class="divider"></div>

  <div class="portrait" role="img" aria-label="Portrait photo of the workshop leader"></div>

  <h2 class="contact-name">Mara Vollbeck</h2>
  <svg class="contact-icon" style="top:1036px" width="26" height="26" viewBox="0 0 26 26" aria-hidden="true">
    <circle cx="13" cy="13" r="11.5" fill="none" stroke="var(--brand-green)" stroke-width="2"/>
    <rect x="9" y="6" width="8" height="14" rx="1.5" fill="none" stroke="var(--brand-blue)" stroke-width="1.8"/>
  </svg>
  <p class="contact-phone">303-417-6652</p>
  <svg class="contact-icon" style="top:1073px" width="26" height="26" viewBox="0 0 26 26" aria-hidden="true">
    <circle cx="13" cy="13" r="11.5" fill="none" stroke="var(--brand-green)" stroke-width="2"/>
    <rect x="7" y="8.5" width="12" height="9" fill="var(--brand-blue)"/>
    <path d="M7,8.5 L13,13.5 L19,8.5" fill="none" stroke="#fff" stroke-width="1.2"/>
  </svg>
  <p class="contact-email">mara@brightwell-daily-craft.com</p>

  <svg class="footer-wave" width="1058" height="1368" viewBox="0 0 1058 1368" aria-hidden="true">
    <path d="M0,1234 Q500,1300 1058,1220 V1368 H0 Z" fill="var(--brand-blue)"/>
    <path d="M0,1222 Q500,1290 1058,1208" fill="none" stroke="var(--brand-green)" stroke-width="6"/>
  </svg>

  <div class="price-badge">
    <p class="price">$45</p>
    <p class="note">All materials are<br>provided.</p>
  </div>

  <p class="brand-name"><span class="mark"></span>Brightwell Daily Craft</p>

  <p class="website">
    <svg width="32" height="32" viewBox="0 0 32 32" aria-hidden="true">
      <circle cx="16" cy="16" r="15" fill="#fff"/>
      <circle cx="16" cy="16" r="11" fill="var(--brand-green)"/>
      <path d="M5,16 H27 M16,5 V27 M16,5 C10,10 10,22 16,27 M16,5 C22,10 22,22 16,27" fill="none" stroke="#fff" stroke-width="1.3"/>
    </svg>brightwell-daily-craft.com
  </p>
</div>
</body>
</html>
```